Design the 21st Golden Reel Indie Screen Week Poster. Think modern, chic, cool, film, movies - driving people to the film festival - the film festivla is in San Francisco and the SF East Bay. Our logo is attached. Dates will be determined soon . please use - November 2 - 11, 2018 (for placement) Keep in mind abstract, chic, modern - eye catching. website is www.grisw.example

Target Market(s)

25 - 45 year old - upper middle class

Industry/Entity Type

Film Production

Colors

Designer to choose colors to be used in the design.

Requirements
Must have
• logo (attached) www.grisw.example - chic modern design
Nice to have
• best coolest poster ever!
Should not have
• CLIP ART!!!

```html
<!DOCTYPE html>
<html lang="en">
<head>
<meta charset="UTF-8">
<title>21st Golden Reel Indie Screen Week</title>
<link href="https://fonts.googleapis.com/css2?family=Kanit:wght@600;800&family=Kaushan+Script&display=swap" rel="stylesheet">
<style>
  :root {
    --curtain-deep: #4a0508;
    --curtain-red: #9c1418;
    --wall-brown: #6a4a36;
    --wall-dark: #3a2418;
    --title-pink: #e8336e;
    --glow-pink: rgba(255, 60, 150, 0.85);
    --number-yellow: #c9c21c;
    --glow-yellow: rgba(240, 230, 60, 0.8);
    --label-orange: #f7985c;
    --glow-orange: rgba(255, 120, 40, 0.85);
    --outline: #f4ecf2;
    --info-cream: #fbeee4;
  }
  html, body {
    margin: 0;
    padding: 0;
    width: 1200px;
    height: 1200px;
    overflow: hidden;
    background: var(--curtain-deep);
  }
  .poster {
    position: relative;
    width: 1200px;
    height: 1200px;
    overflow: hidden;
  }
  .stage-scene {
    position: absolute;
    inset: 0;
    background:
      radial-gradient(ellipse 420px 560px at 50% 48%, var(--wall-brown) 0%, var(--wall-dark) 70%, transparent 100%),
      linear-gradient(90deg, var(--curtain-deep) 0%, var(--curtain-red) 10%, var(--curtain-deep) 18%, var(--wall-dark) 26%, var(--wall-dark) 74%, var(--curtain-deep) 82%, var(--curtain-red) 90%, var(--curtain-deep) 100%);
  }
  .projector {
    position: absolute;
    left: 176px;
    top: 1010px;
    width: 592px;
    height: 190px;
    background: radial-gradient(ellipse at 60% 40%, #8a8a90 0%, #4a4a50 55%, rgba(60,40,40,0) 100%);
  }
  .popcorn {
    position: absolute;
    left: 800px;
    top: 910px;
    width: 400px;
    height: 290px;
    background: radial-gradient(ellipse at 55% 35%, #f4e08a 0%, #e8c866 45%, #d9d4cc 75%, rgba(200,190,180,0) 100%);
  }
  .brand-mark {
    position: absolute;
    top: 36px;
    left: 36px;
    display: flex;
    align-items: center;
    gap: 10px;
    font-family: "Kanit", sans-serif;
    font-weight: 600;
    font-size: 22px;
    line-height: 1;
    color: var(--info-cream);
  }
  .brand-dot {
    width: 18px;
    height: 18px;
    border-radius: 50%;
    background: var(--info-cream);
  }
  .title-block {
    position: absolute;
    left: 0;
    top: 0;
    width: 1200px;
    margin: 0;
    text-align: center;
  }
  .edition {
    position: absolute;
    top: 96px;
    left: 0;
    width: 1200px;
    font-family: "Kanit", sans-serif;
    font-weight: 800;
    font-size: 104px;
    line-height: 1;
    color: var(--number-yellow);
    -webkit-text-stroke: 6px var(--outline);
    paint-order: stroke fill;
    text-shadow: 0 0 30px var(--glow-yellow), 0 0 60px var(--glow-yellow);
  }
  .edition sup {
    font-size: 52px;
    vertical-align: 38px;
  }
  .event-name {
    position: absolute;
    left: 0;
    width: 1200px;
    font-family: "Kaushan Script", cursive;
    font-size: 150px;
    line-height: 1;
    color: var(--title-pink);
    -webkit-text-stroke: 8px var(--outline);
    paint-order: stroke fill;
    text-shadow: 0 0 24px var(--glow-pink), 0 0 50px var(--glow-pink);
    transform: skewX(-6deg);
  }
  .line-one { top: 240px; }
  .line-two { top: 410px; }
  .line-three { top: 580px; }
  .event-type {
    position: absolute;
    top: 776px;
    left: 0;
    width: 1200px;
    font-family: "Kanit", sans-serif;
    font-weight: 800;
    font-size: 96px;
    line-height: 1;
    letter-spacing: -2px;
    color: var(--label-orange);
    -webkit-text-stroke: 6px var(--outline);
    paint-order: stroke fill;
    text-shadow: 0 0 24px var(--glow-orange), 0 0 50px var(--glow-orange);
  }
  .event-info {
    position: absolute;
    top: 898px;
    left: 250px;
    width: 540px;
    text-align: center;
    font-family: "Kanit", sans-serif;
    color: var(--info-cream);
    text-shadow: 0 0 14px rgba(0,0,0,0.8);
  }
  .event-dates {
    margin: 0;
    font-weight: 800;
    font-size: 34px;
    line-height: 1.1;
    letter-spacing: 1px;
  }
  .event-place {
    margin: 4px 0 0;
    font-weight: 600;
    font-size: 20px;
    line-height: 1.2;
    letter-spacing: 2px;
    text-transform: uppercase;
  }
  .event-web {
    margin: 4px 0 0;
    font-weight: 600;
    font-size: 20px;
    line-height: 1.2;
    color: var(--label-orange);
  }
</style>
</head>
<body>
  <div class="poster">
    <div class="stage-scene" role="img" aria-label="Theatre stage with red velvet curtains tied back by tasselled ropes, framing a warmly lit brick wall"></div>
    <div class="projector" role="img" aria-label="Vintage film projector with two reels"></div>
    <div class="popcorn" role="img" aria-label="White bucket overflowing with buttered popcorn"></div>

    <div class="brand-mark"><span class="brand-dot"></span>Golden Reel Indie Screen Week</div>

    <h1 class="title-block">
      <span class="edition">21<sup>ST</sup></span>
      <span class="event-name line-one">Golden</span>
      <span class="event-name line-two">Reel Indie</span>
      <span class="event-name line-three">Screen</span>
      <span class="event-type">WEEK</span>
    </h1>

    <div class="event-info">
      <p class="event-dates">November 2 – 11, 2018</p>
      <p class="event-place">San Francisco &amp; the East Bay</p>
      <p class="event-web">www.grisw.example</p>
    </div>
  </div>
</body>
</html>
```